KRM/DOLV JV

We need a business card design for a joint venture construction company. We have two logos that need to appear and need to be cleaned up. We are looking for a simple design with a white background and black lettering. The company name is K. Marlowitz, Inc./D. Olvera Construction Corp. J.V.

The website is www.krmdolv.com

Please indicate spaces for phone; fax and cell. For this mockup use the following info:

Rob Kessing
Project Enginner
2817 Route 4
Castleton, NY 12987
robkrmdolv@mailbrook.com
Office: 555-014-38826
Fax: 555-014-6190
Cell: 555-019-4473

Please note; the logos themselves should not include the company names but the card should include the name of the company - K. Marlowitz, Inc./D. Olvera Construction Corp., J.V. 

Also, the logo should appear alphabetically KRM first, then DOLV, but they should be the same size.

Industry/Entity Type

Construction

Requirements
Should not have
• The logos should not include the company name; please crop that from the image.

```html
<!DOCTYPE html>
<html lang="en">
<head>
<meta charset="utf-8">
<title>KRM/DOLV JV — Business Card</title>
<link rel="stylesheet" href="https://fonts.googleapis.com/css2?family=Questrial&family=Oswald:wght@600&display=swap">
<style>
  :root {
    --page-bg: #e9e7e4;
    --card-bg: #ffffff;
    --brand-red: #a5232b;
    --brand-navy: #232a6e;
    --ink: #111111;
  }
  * { box-sizing: border-box; margin: 0; padding: 0; }
  html, body {
    width: 1200px; height: 800px; overflow: hidden;
    background: var(--page-bg);
  }
  .card {
    position: absolute; left: 100px; top: 114px;
    width: 1000px; height: 572px;
    background: var(--card-bg);
    box-shadow: 0 10px 30px rgba(0,0,0,0.18);
    overflow: hidden;
  }
  .card__band {
    position: absolute; left: 0; right: 0; bottom: 0; height: 84px;
    background: var(--brand-navy);
    border-top: 7px solid var(--brand-red);
  }
  .logos {
    position: absolute; left: 62px; top: 40px;
    display: flex; align-items: center; gap: 44px;
  }
  .logo {
    display: flex; align-items: center; gap: 14px;
    font-family: "Questrial", sans-serif;
    font-size: 72px; line-height: 1; letter-spacing: 2px;
  }
  .logo__square { width: 34px; height: 34px; display: block; }
  .logo--krm { color: var(--brand-red); }
  .logo--krm .logo__square { background: var(--brand-red); }
  .logo--dolv { color: var(--brand-navy); }
  .logo--dolv .logo__square { background: var(--brand-navy); }
  .company-name {
    position: absolute; left: 62px; top: 128px;
    font-family: "Oswald", sans-serif; font-weight: 600;
    font-size: 21px; line-height: 1.2; letter-spacing: 0.3px; text-transform: uppercase;
    color: var(--ink);
  }
  .person { position: absolute; left: 112px; top: 184px; font-family: "Questrial", sans-serif; }
  .person__name { color: var(--brand-red); font-size: 30px; line-height: 1.1; }
  .person__title { color: var(--ink); font-size: 19px; line-height: 1.2; margin-top: 2px; }
  .contact {
    position: absolute; left: 112px; top: 256px;
    list-style: none; font-family: "Questrial", sans-serif;
    font-size: 25px; line-height: 31px; color: var(--ink);
  }
  .contact__item { display: flex; align-items: flex-start; gap: 10px; }
  .contact__icon { width: 26px; height: 26px; flex: none; margin-top: 3px; fill: var(--brand-red); }
</style>
</head>
<body>
  <main class="card" aria-label="Business card for KRM/DOLV JV">
    <div class="logos">
      <div class="logo logo--krm"><span>KRM</span><span class="logo__square"></span></div>
      <div class="logo logo--dolv"><span class="logo__square"></span><span>DOLV</span></div>
    </div>
    <p class="company-name">K. Marlowitz, Inc./D. Olvera Construction Corp. J.V.</p>

    <div class="person">
      <p class="person__name">Rob Kessing</p>
      <p class="person__title">Project Enginner</p>
    </div>

    <ul class="contact">
      <li class="contact__item">
        <svg class="contact__icon" viewBox="0 0 24 24" aria-hidden="true"><path d="M12 3 2 12h3v9h5v-6h4v6h5v-9h3z"/></svg>
        <span>2817 Route 4<br>Castleton, NY 12987</span>
      </li>
      <li class="contact__item">
        <svg class="contact__icon" viewBox="0 0 24 24" aria-hidden="true"><path d="M2 5h20v14H2z M4 7v1l8 5 8-5V7l-8 5z" fill-rule="evenodd"/></svg>
        <span>robkrmdolv@mailbrook.com</span>
      </li>
      <li class="contact__item">
        <svg class="contact__icon" viewBox="0 0 24 24" aria-hidden="true"><path d="M6.6 10.8a15 15 0 0 0 6.6 6.6l2.2-2.2c.3-.3.7-.4 1-.2 1.1.4 2.3.6 3.6.6.6 0 1 .4 1 1V20c0 .6-.4 1-1 1A17 17 0 0 1 3 4c0-.6.4-1 1-1h3.5c.6 0 1 .4 1 1 0 1.3.2 2.5.6 3.6.1.3 0 .7-.2 1z"/></svg>
        <span>555-014-38826</span>
      </li>
      <li class="contact__item">
        <svg class="contact__icon" viewBox="0 0 24 24" aria-hidden="true"><path d="M7 2h8l3 3v5H7z M4 11h16v8h-3v3H7v-3H4z M9 15v5h6v-5z" fill-rule="evenodd"/></svg>
        <span>555-014-6190</span>
      </li>
      <li class="contact__item">
        <svg class="contact__icon" viewBox="0 0 24 24" aria-hidden="true"><path d="M7 2h10v20H7z M9 4v10h6V4z M9 16h2v2H9z M13 16h2v2h-2z" fill-rule="evenodd"/></svg>
        <span>555-019-4473</span>
      </li>
    </ul>

    <div class="card__band"></div>
  </main>
</body>
</html>
```